"Vows and Farewells by Meg" Web Site

I would like a web site designed for my funeral and wedding celebrancy business. My logo was designed by Artboard Hive (attached). I have written content of the web pages for reference (attached). I have attached logos designed through artboard hive and photos.
I am sure what else to write in a project description and would welcome suggestions

Target Market(s)

for marriages - brides and grooms, for funerals - families who have lost a loved one

Industry/Entity Type

Wedding Planner

Number of Pages Required

4 page

Font styles to use
Sans Serif

Colors
886aae
3277b5
33a6d7
a64599
e34096

Requirements
Must have
• a call to action (contact me) throughout
Nice to have
• nil
Should not have
• no morbid images

```html
<!DOCTYPE html>
<html lang="en">
<head>
<meta charset="utf-8">
<title>Vows and Farewells by Meg</title>
<link href="https://fonts.googleapis.com/css2?family=Great+Vibes&display=swap" rel="stylesheet">
<style>
:root{
  --purple:#886aae;
  --plum:#a64599;
  --navy-blue:#3277b5;
  --sky:#33a6d7;
  --pink:#e34096;
  --white:#ffffff;
  --ink-logo:#4b2c8f;
  --script:"Great Vibes", cursive;
}
*{margin:0;padding:0;box-sizing:border-box}
html,body{width:1200px;height:2317px;overflow:hidden}
body{position:relative;background:var(--white);font-family:var(--script);color:var(--white)}
.abs{position:absolute}

/* header */
.site-header{left:0;top:0;width:1200px;height:183px;background:var(--white)}
.brand-mark{left:560px;top:28px;width:80px;height:80px;border-radius:50%;background:var(--purple);opacity:.35}
.brand-name{left:0;top:116px;width:1200px;text-align:center;font-size:54px;color:var(--ink-logo);line-height:1}

/* nav */
.main-nav{left:0;top:183px;width:1200px;height:62px;display:flex;background:var(--purple)}
.main-nav a{flex:1;display:flex;align-items:center;justify-content:center;gap:10px;color:var(--white);text-decoration:none;font-size:38px}
.main-nav a.is-active{background:var(--sky)}

/* hero */
.hero{left:0;top:245px;width:1200px;height:552px}
.hero-photo{left:0;top:0;width:1200px;height:552px;background:linear-gradient(90deg,#e8a7b2 0%,#c05a7c 18%,#b07a6c 38%,#8d7a6c 50%,#9a8b7e 75%,#7f7266 100%)}
.hero-title{left:620px;top:70px;width:500px;text-align:center;font-size:84px;line-height:1.1;text-shadow:0 4px 10px rgba(0,0,0,.55)}
.btn{display:flex;align-items:center;justify-content:center;color:var(--white);font-size:26px}
.btn-location{left:667px;top:272px;width:200px;height:39px;background:var(--plum);gap:10px;justify-content:flex-start;padding-left:14px}
.btn-appointment{left:890px;top:272px;width:202px;height:39px;background:var(--navy-blue)}
.hero-call{left:620px;top:330px;width:540px;text-align:center;font-size:66px;text-shadow:0 4px 10px rgba(0,0,0,.55)}
.btn-phone{left:667px;top:413px;width:425px;height:48px;background:var(--pink);font-size:40px;gap:30px}
.rule{left:0;width:1200px;height:9px;background:var(--purple)}

/* about */
.about-text{left:51px;top:940px;width:655px;color:var(--sky);font-size:24px;line-height:1.15}
.about-text p{margin-bottom:24px}
.portrait-frame{left:763px;top:921px;width:393px;height:479px;border:14px solid var(--pink)}
.portrait{left:731px;top:896px;width:374px;height:461px;background:linear-gradient(160deg,#cfd6e0 0%,#b89a72 40%,#3a3a3a 100%)}
.btn-contact{left:340px;top:1443px;width:521px;height:63px;background:var(--sky);font-size:38px}

/* contact */
.contact{left:0;top:1557px;width:1200px;height:708px}
.contact-photo{left:0;top:0;width:1200px;height:708px;background:linear-gradient(180deg,#6b6f7a 0%,#5b6470 35%,#6e6a68 60%,#8a7a6c 100%)}
.contact-shade{left:0;top:0;width:1200px;height:708px;background:rgba(60,45,70,.35)}
.contact-title{left:0;top:40px;width:1200px;text-align:center;font-size:92px}
.field{background:rgba(51,166,215,.78);color:var(--white);font-size:22px;padding:14px 14px}
.f-name{left:46px;top:201px;width:260px;height:59px}
.f-email{left:329px;top:201px;width:260px;height:59px}
.f-address{left:46px;top:272px;width:260px;height:59px}
.f-number{left:329px;top:272px;width:260px;height:59px}
.f-message{left:46px;top:343px;width:543px;height:121px}
.btn-send{left:46px;top:476px;width:260px;height:59px;background:var(--purple);font-size:36px}
.info{left:770px;font-size:42px;line-height:1.15}
.info-icon{left:708px}
.info-address{top:200px}
.info-phone{top:393px}
.info-email{top:490px}

/* footer */
.site-footer{left:0;top:2265px;width:1200px;height:52px;background:var(--purple);display:flex;align-items:center;justify-content:center;gap:16px;font-size:30px}
.site-footer .muted{opacity:.6}
</style>
</head>
<body>

<header class="site-header abs">
  <div class="brand-mark abs"></div>
  <div class="brand-name abs">Vows and Farewells by Meg</div>
</header>

<nav class="main-nav abs">
  <a class="is-active">Home</a>
  <a>About</a>
  <a>Services
    <svg width="12" height="10" viewBox="0 0 12 10"><path d="M1 1 L6 9 L11 1" fill="none" stroke="#fff" stroke-width="1.5"/></svg>
  </a>
  <a>Contact</a>
</nav>

<section class="hero abs">
  <div class="hero-photo abs" role="img" aria-label="Bouquet of pink and peach roses on a rustic wooden table"></div>
  <h1 class="hero-title abs" style="font-weight:400">Get Your<br>Services Now!</h1>
  <div class="btn btn-location abs">
    <svg width="12" height="16" viewBox="0 0 12 16"><path d="M6 0C2.7 0 0 2.6 0 5.9 0 10 6 16 6 16s6-6 6-10.1C12 2.6 9.3 0 6 0zm0 8.2A2.3 2.3 0 1 1 6 3.6a2.3 2.3 0 0 1 0 4.6z" fill="#fff"/></svg>
    Select Location
    <svg style="margin-left:auto;margin-right:12px" width="8" height="6" viewBox="0 0 8 6"><path d="M0 0 L4 6 L8 0" fill="none" stroke="#fff"/></svg>
  </div>
  <div class="btn btn-appointment abs">Get an appointment</div>
  <div class="hero-call abs">Or Call Me Now!</div>
  <div class="btn btn-phone abs">
    <svg width="28" height="28" viewBox="0 0 24 24"><path d="M6.6 10.8a15.1 15.1 0 0 0 6.6 6.6l2.2-2.2c.3-.3.7-.4 1-.2 1.1.4 2.3.6 3.6.6.6 0 1 .4 1 1V20c0 .6-.4 1-1 1A17 17 0 0 1 3 4c0-.6.4-1 1-1h3.5c.6 0 1 .4 1 1 0 1.3.2 2.5.6 3.6.1.3 0 .7-.2 1z" fill="#fff"/></svg>
    (+61) 0400123987
  </div>
</section>
<div class="rule abs" style="top:797px"></div>

<section class="about">
  <div class="about-text abs">
    <p>Thank you for visiting ‘Vows and Farewells by Meg’. Whether you are planning a wedding with the love of your life, a funeral to celebrate the life of a loved one or one of many other love and life celebrations, I am glad that you came to ‘Vows and Farewells by Meg’.</p>
    <p>My name is Meg Harrowfield and I am the owner of this business. My mission is to work with you to create a marriage, funeral or celebration service that truly celebrates love and life in an authentic way. Your way!</p>
    <p>I am legally authorised by the Commonwealth Attorney General’s department to perform marriages across Australia and have completed a certificate IV in Celebrancy which included Marriage celebrancy units and Funeral celebrancy units</p>
    <p>My commitment to you is that I will spend time with you, get to know you, listen to your dreams and desires for your celebration. We can then create a service that is unique, special and memorable.</p>
  </div>
  <div class="portrait-frame abs"></div>
  <div class="portrait abs" role="img" aria-label="Portrait of the celebrant smiling at an event"></div>
  <div class="btn btn-contact abs">Please contact me to discuss your needs</div>
</section>
<div class="rule abs" style="top:1548px"></div>

<section class="contact abs">
  <div class="contact-photo abs" role="img" aria-label="Celebrant with arms outstretched at a beach wedding"></div>
  <div class="contact-shade abs"></div>
  <h2 class="contact-title abs" style="font-weight:400">Contact Me</h2>

  <div class="field f-name abs">Name:</div>
  <div class="field f-email abs">Email:</div>
  <div class="field f-address abs">Address:</div>
  <div class="field f-number abs">Contact # :</div>
  <div class="field f-message abs">Message:</div>
  <div class="btn btn-send abs">Send</div>

  <svg class="info-icon abs" style="top:205px" width="42" height="40" viewBox="0 0 24 22"><path d="M12 1 1 11h3v10h6v-6h4v6h6V11h3z" fill="#33a6d7"/></svg>
  <div class="info info-address abs">Meg Harrowfield<br>P.O Box 812, Larkmoor<br>6950, Western Australia</div>

  <svg class="info-icon abs" style="top:402px;left:716px" width="32" height="32" viewBox="0 0 24 24"><path d="M6.6 10.8a15.1 15.1 0 0 0 6.6 6.6l2.2-2.2c.3-.3.7-.4 1-.2 1.1.4 2.3.6 3.6.6.6 0 1 .4 1 1V20c0 .6-.4 1-1 1A17 17 0 0 1 3 4c0-.6.4-1 1-1h3.5c.6 0 1 .4 1 1 0 1.3.2 2.5.6 3.6.1.3 0 .7-.2 1z" fill="#33a6d7"/></svg>
  <div class="info info-phone abs">Phone: (+61) 0400123987</div>

  <svg class="info-icon abs" style="top:503px;left:714px" width="38" height="28" viewBox="0 0 24 18"><path d="M0 2v14h24V2L12 10z M1 0l11 8 11-8z" fill="#33a6d7"/></svg>
  <div class="info info-email abs">Email: meg1@vowsmail.net.au</div>
</section>

<footer class="site-footer abs">
  <span class="muted">Copyright 2018</span><span class="muted">|</span><span>Vows and Farewells by Meg</span>
</footer>

</body>
</html>
```